Plakate für Sinfonischer Chor der Tonhalle-Kantorei Elmhorst
Zielgruppe
Die Tonhalle-Kantorei Elmhorst und deren Sinfonischer Chor führt chorsinfonische Werke mit Chor- und Orchester und Solisten auf. Weitere Infos unter: https://www.tonhalle-kantorei-elmhorst.de/
Aufgabenstellung
Ein frisches und modern gestaltetes Plakat soll für das nächste Konzertprojekt entstehen. Aufgeführt wird:
Wendlinger Es Dur Messe
Trøvik Lantern Mass
Als Gestaltungselement kommen neben Fotos vom Chor, ein Sonnenaufgang, eine Stadt oder eine Darstellung von Sphären/Weltall in Frage. Fotos vom Chor liegen in professioneller Qualität vor.
Neben dem Plakat, können Folgeaufträge für Flyer und Programmheft entstehen.
Sinfonischer Chor der Tonhalle-Kantorei Elmhorst
Kinoensemble Waldenfels
Helena Marakou, Sopran
Wiktoria Lessenko, Alt
Florian Wettbrak, Tenor
Ulrich Damm, Tenor
Tobias Krenner, Bass
Eik Halvorsen, Dirigent
17.00 Uhr
Lindenforum Elmhorst

```html
<!DOCTYPE html>
<html lang="de">
<head>
<meta charset="utf-8">
<title>Wendlinger · Trøvik – Konzertplakat</title>
<link rel="stylesheet" href="https://fonts.googleapis.com/css2?family=Roboto+Condensed:wght@300;400;700&family=Roboto:wght@400;700&display=swap">
<style>
  :root{
    --ink:#ffffff;
    --bg-deep:#0f0906;
    --bg-rust:#5a2a12;
    --glow-core:#fff1d6;
    --glow-amber:#f0a04a;
    --glow-copper:#a8501c;
  }
  html,body{margin:0;padding:0;overflow:hidden;background:var(--bg-deep);}
  .poster{
    position:relative;width:848px;height:1200px;overflow:hidden;
    color:var(--ink);font-family:"Roboto Condensed",sans-serif;
  }
  .poster__visual{position:absolute;inset:0;}
  .poster__visual svg{display:block;width:100%;height:100%;}
  .line{position:absolute;left:0;width:100%;margin:0;line-height:1;text-align:center;white-space:nowrap;}
  .work__composer{font-weight:700;font-size:90px;letter-spacing:1px;}
  .work__title{font-weight:400;font-size:36px;}

  .event__block{position:absolute;top:822px;margin:0;text-align:center;
    font-family:"Roboto",sans-serif;font-weight:700;font-size:50px;line-height:1.12;letter-spacing:.5px;white-space:nowrap;}
  .event__block span{display:block;}
  .event__date{left:62px;width:300px;}
  .event__venue{right:56px;width:370px;}

  .ensembles{font-family:"Roboto",sans-serif;font-weight:700;font-size:15.5px;letter-spacing:.3px;}
  .soloist{position:absolute;margin:0;font-family:"Roboto",sans-serif;font-weight:400;font-size:13.5px;line-height:1;white-space:nowrap;}
  .host{font-weight:400;font-size:32px;letter-spacing:2px;}
</style>
</head>
<body>
<main class="poster">
  <div class="poster__visual" role="img" aria-label="Foto: dunkler, gewölbter Tunnel mit Gleisen, in dessen Mitte ein leuchtender Funkenkreis glüht">
    <svg viewBox="0 0 848 1200" preserveAspectRatio="none">
      <defs>
        <radialGradient id="tunnelLight" cx="424" cy="650" r="560" gradientUnits="userSpaceOnUse">
          <stop offset="0" stop-color="var(--glow-core)"/>
          <stop offset=".08" stop-color="var(--glow-amber)"/>
          <stop offset=".3" stop-color="var(--glow-copper)"/>
          <stop offset=".6" stop-color="var(--bg-rust)"/>
          <stop offset="1" stop-color="var(--bg-deep)"/>
        </radialGradient>
        <linearGradient id="floorShade" x1="0" y1="0" x2="0" y2="1">
          <stop offset="0" stop-color="#000" stop-opacity="0"/>
          <stop offset=".5" stop-color="#000" stop-opacity="0"/>
          <stop offset=".7" stop-color="#000" stop-opacity=".55"/>
          <stop offset="1" stop-color="#000" stop-opacity=".85"/>
        </linearGradient>
      </defs>
      <rect width="848" height="1200" fill="url(#tunnelLight)"/>
      <rect width="848" height="1200" fill="url(#floorShade)"/>
    </svg>
  </div>

  <section class="programme">
    <h1 class="line work__composer" style="top:82px">WENDLINGER</h1>
    <p class="line work__title" style="top:176px">Es Dur Messe</p>
    <h1 class="line work__composer" style="top:276px">TRØVIK</h1>
    <p class="line work__title" style="top:372px">Lantern Mass</p>
  </section>

  <section class="event">
    <p class="event__block event__date"><span>15.10.2023</span><span>17.00 UHR</span></p>
    <p class="event__block event__venue"><span>LINDENFORUM</span><span>ELMHORST</span></p>
  </section>

  <section class="credits">
    <p class="line ensembles" style="top:984px;text-align:left;left:60px">SINFONISCHER CHOR DER TONHALLE-KANTOREI ELMHORST</p>
    <p class="line ensembles" style="top:984px;text-align:right;left:auto;right:70px;width:auto">KINOENSEMBLE WALDENFELS</p>
    <p class="soloist" style="top:1019px;left:96px">HELENA MARAKOU, Sopran</p>
    <p class="soloist" style="top:1043px;left:96px">WIKTORIA LESSENKO, Alt</p>
    <p class="soloist" style="top:1019px;left:330px">FLORIAN WETTBRAK, Tenor</p>
    <p class="soloist" style="top:1043px;left:330px">ULRICH DAMM, Tenor</p>
    <p class="soloist" style="top:1019px;left:564px">TOBIAS KRENNER, Bass</p>
    <p class="soloist" style="top:1043px;left:564px">EIK HALVORSEN, Dirigent</p>
  </section>

  <footer>
    <p class="line host" style="top:1118px">TONHALLE-KANTOREI ELMHORST</p>
  </footer>
</main>
</body>
</html>
```